Zielgruppe
Steuerberater, Zielgruppe: Mandanten
Aufgabenstellung
Es sollten keine Balken an den Rändern vorhanden sein, so dass das Briefpapier mit dem eigenen Farbdrucker bedruckt werden kann.
-Keine Balken an den Rändern
-Wir wollen kein Briefpapier bedrucken lassen, soll mit dem eigenen Drucker bedruckbar sein
Die Schriftart CG Omega sollte installiert sein, für die korrekte Darstellung.

```html
<!DOCTYPE html>
<html lang="de">
<head>
<meta charset="utf-8">
<title>Briefbogen Kanzlei Berlant</title>
<link rel="stylesheet" href="https://fonts.googleapis.com/css2?family=Mulish:wght@400;700&display=swap">
<style>
  :root {
    --navy: #1b2a55;
    --ink: #3a3a3a;
    --paper: #ffffff;
  }
  html, body {
    margin: 0;
    padding: 0;
    overflow: hidden;
    background: var(--paper);
  }
  .letterhead {
    position: relative;
    width: 848px;
    height: 1200px;
    overflow: hidden;
    background: var(--paper);
    font-family: "Mulish", sans-serif;
    color: var(--ink);
  }
  .brand-name {
    position: absolute;
    left: 551px;
    top: 58px;
    margin: 0;
    font-size: 37px;
    font-weight: 400;
    letter-spacing: 0.5px;
    color: var(--navy);
    white-space: nowrap;
  }
  .sender-line {
    position: absolute;
    left: 106px;
    top: 192px;
    font-size: 11px;
    white-space: nowrap;
  }
  .sender-line strong {
    color: var(--navy);
    font-weight: 700;
  }
  .sender-line .sep {
    margin: 0 6px;
  }
  .contact-column {
    position: absolute;
    left: 673px;
    top: 190px;
    font-size: 12px;
    line-height: 18.5px;
  }
  .contact-column p {
    margin: 0;
  }
  .contact-column .person-name {
    color: var(--navy);
    font-weight: 700;
  }
  .contact-column .block {
    margin-bottom: 10px;
  }
  .contact-column .block-address {
    margin-top: 18px;
  }
  .contact-column .label {
    display: inline-block;
    width: 53px;
  }
  .bank-footer {
    position: absolute;
    left: 28px;
    top: 1175px;
    font-size: 10.3px;
    white-space: nowrap;
  }
  .bank-footer strong {
    font-weight: 700;
  }
  .bank-footer .tax-id {
    margin-left: 8px;
  }
</style>
</head>
<body>
<div class="letterhead">
  <h1 class="brand-name">Kanzlei Berlant</h1>

  <div class="sender-line">
    <strong>Kanzlei Berlant</strong><span class="sep">I</span>Lindenweg 14<span class="sep">I</span>71234 Talhausen
  </div>

  <div class="contact-column">
    <div class="block">
      <p class="person-name">Tamer Berlant</p>
      <p>Diplom-Kaufmann</p>
      <p>Steuerberater</p>
    </div>
    <div class="block">
      <p class="person-name">Aydin Berlant</p>
      <p>Rechtsanwalt</p>
      <p>Fachanwalt für Steuerrecht</p>
    </div>
    <div class="block block-address">
      <p>Lindenweg 14</p>
      <p>71234 Talhausen</p>
    </div>
    <div class="block">
      <p><span class="label">Telefon:</span>07155 – 412203</p>
      <p><span class="label">Telefax:</span>07155 – 412205</p>
    </div>
    <div class="block">
      <p>mail@kanzlei-berlant.de</p>
      <p>www.kanzlei-berlant.de</p>
    </div>
  </div>

  <div class="bank-footer">
    <strong>Bankverbindung</strong> I Kanzlei Berlant GbR • Talbank AG • IBAN: DE12 3456 7890 1234 5678 90 • BIC: TALBDEFFXXX
    <span class="tax-id"><strong>Umsatzsteuer-ID</strong> I DE123456789</span>
  </div>
</div>
</body>
</html>
```